Brookline Wealth Guidance - Employer Benefit Brochure

We need to design a professional looking brochure that we can present to our existing client base, and assist in attracting new clients.
The current information is just provided in a word document, but we need to improve significantly.
The audience would be business leaders, HR decision makers and member policy committee members

Industry/Entity Type

Business

Font styles to use
Sans Serif

Colors
0255a3
f37122

```html
<!DOCTYPE html>
<html lang="en">
<head>
<meta charset="utf-8">
<title>Brookline Wealth Guidance – Employer Benefits Partnership</title>
<link rel="stylesheet" href="https://fonts.googleapis.com/css2?family=Source+Sans+3:wght@400;600;700&display=swap">
<style>
  :root {
    --blue: #2b52a8;
    --orange: #f25f1f;
    --white: #ffffff;
    --photo-light: #eef0f2;
    --photo-mid: #d8dadd;
  }
  * { margin: 0; padding: 0; box-sizing: border-box; }
  html, body { width: 1200px; height: 994px; overflow: hidden; background: var(--white); }
  body { position: relative; font-family: "Source Sans 3", "Myriad Pro", Arial, sans-serif; }

  .brochure { position: absolute; left: 107px; top: 115px; width: 990px; height: 765px; }

  /* Left panel */
  .panel-left { position: absolute; left: 0; top: 0; width: 329px; height: 765px; }
  .hero-image {
    position: absolute; left: 0; top: 3px; width: 329px; height: 319px;
    background: linear-gradient(135deg, var(--white) 0%, var(--photo-light) 45%, var(--photo-mid) 100%);
  }
  .value-box {
    position: absolute; left: 0; top: 322px; width: 329px; height: 443px;
    background: var(--blue); padding: 58px 28px 0 53px;
  }
  .value-title { color: var(--orange); font-size: 20px; font-weight: 700; letter-spacing: -0.2px; margin-bottom: 12px; margin-left: 0; }
  .value-list { list-style: none; }
  .value-list li {
    position: relative; color: var(--white); font-size: 11px; line-height: 15px;
    padding-left: 35px; margin-bottom: 15px; text-align: justify;
  }
  .value-list svg { position: absolute; left: 8px; top: 3px; width: 15px; height: 17px; }

  /* Middle panel */
  .panel-middle { position: absolute; left: 329px; top: 0; width: 324px; height: 765px; text-align: center; }
  .contact { position: absolute; top: 422px; left: 0; width: 324px; color: var(--blue); }
  .contact-title { color: var(--orange); font-size: 22px; font-weight: 700; margin-bottom: 20px; }
  .contact p { font-size: 15px; line-height: 21px; }
  .contact .phone { margin-bottom: 20px; }
  .contact .web { font-weight: 700; margin-bottom: 20px; }
  .contact .address strong { font-weight: 700; }
  .rule-blue { position: absolute; left: 0; top: 678px; width: 324px; height: 4px; background: var(--blue); }
  .rule-orange { position: absolute; left: 0; top: 684px; width: 324px; height: 2px; background: var(--orange); }
  .mark-small {
    position: absolute; left: 137px; top: 652px; width: 55px; height: 53px;
    background: var(--blue); border: 3px solid var(--orange);
  }

  /* Right panel (cover) */
  .panel-cover { position: absolute; left: 653px; top: 0; width: 337px; height: 765px; background: var(--orange); overflow: hidden; }
  .cover-top { position: absolute; left: 0; top: 0; }
  .mark-large {
    position: absolute; left: 78px; top: 100px; width: 152px; height: 143px;
    background: var(--blue); border: 5px solid #f6a21a;
  }
  .company-name {
    position: absolute; left: 0; top: 276px; width: 300px;
    color: var(--blue); font-size: 20px; font-weight: 700; line-height: 27px; text-align: center; text-transform: uppercase;
  }
  .cover-title {
    position: absolute; left: 0; top: 393px; width: 300px;
    color: var(--white); font-size: 35px; font-weight: 700; line-height: 45px; text-align: center;
  }
</style>
</head>
<body>
<main class="brochure">
  <section class="panel-left">
    <div class="hero-image" role="img" aria-label="Photo of four hands joining puzzle pieces, one piece orange"></div>
    <div class="value-box">
      <h2 class="value-title">OUR VALUE PROPOSITION</h2>
      <ul class="value-list">
        <li><svg viewBox="0 0 15 17"><path d="M0 0 L15 8.5 L0 17 L5 8.5 Z" fill="#f6a21a"/></svg>We endorse the employer’s positioning in the benefits and delivery of their Program</li>
        <li><svg viewBox="0 0 15 17"><path d="M0 0 L15 8.5 L0 17 L5 8.5 Z" fill="#f6a21a"/></svg>We mitigate the legislative and compliance risk with respect to superannuation</li>
        <li><svg viewBox="0 0 15 17"><path d="M0 0 L15 8.5 L0 17 L5 8.5 Z" fill="#f6a21a"/></svg>We lighten the administrative burden so the employer can focus on their core business</li>
        <li><svg viewBox="0 0 15 17"><path d="M0 0 L15 8.5 L0 17 L5 8.5 Z" fill="#f6a21a"/></svg>We provide the employer and employee with a single point of contact</li>
        <li><svg viewBox="0 0 15 17"><path d="M0 0 L15 8.5 L0 17 L5 8.5 Z" fill="#f6a21a"/></svg>We bring a ‘know the market’ capability to ensure best of breed solutions</li>
        <li><svg viewBox="0 0 15 17"><path d="M0 0 L15 8.5 L0 17 L5 8.5 Z" fill="#f6a21a"/></svg>We provide a competitive advantage to help attract and retain the best talent</li>
      </ul>
    </div>
  </section>

  <section class="panel-middle">
    <div class="contact">
      <h2 class="contact-title">CONTACT US</h2>
      <p class="phone">02 9400 6120</p>
      <p class="web">www.brooklinewg.com.au<br>info@brooklinewg.com.au</p>
      <p class="address">14 <strong>Harlow Lane,</strong><br><strong>North Sydney, NSW,</strong> 2060</p>
    </div>
    <div class="rule-blue"></div>
    <div class="rule-orange"></div>
    <div class="mark-small"></div>
  </section>

  <section class="panel-cover">
    <svg class="cover-top" width="337" height="260" viewBox="0 0 337 260">
      <path d="M0 0 H337 V255 H250 V220 H230 V172 H0 Z" fill="var(--blue)"/>
    </svg>
    <div class="mark-large"></div>
    <p class="company-name">Brookline<br>Wealth Guidance</p>
    <h1 class="cover-title">EMPLOYER<br>BENEFITS<br>PARTNERSHIP</h1>
  </section>
</main>
</body>
</html>
```